Cover design for new academic journal on deconstruction and psychoanalysis

We need a cover for a new academic journal on deconstruction and psychoanalysis. The name of the journal is "The Liminal Remainder: A Journal of Deconstruction and Psychoanalysis" (LR) and it is published by the Calloway Ridge University Press(CRP).

Here is a description of the journal on the CRP website:

http://www.callowayridgepress.example.edu/product/The-Liminal-Remainder,482917.aspx

We are looking for a design that is more abstract and does not have icons or photographs of people, especially not photos of Valmont or Kessler. The design should be contemporary with clean lines and simple fonts. Again, it should be abstract, with no icons or iconography.

The cover should simply have the full name of the journal and then "Volume 1, Issue 1, 2014" on the cover and "Vol. 1, No. 1, 2014" on the spine.

Attached you can see some ideas that we rejected from CRP. It is important that you understand that these designs were rejected and are just being offered as examples of what the cover will look like in general, as a template of sorts.

The cover should have a bold abstract design, with a space for the title and "Volume 1, Issue 1, 2014."

Something bold and contemporary.

Academics, scholars and psychoanalysts.

University

Sans Serif

• Must be abstract, bold, have color, and must be contemporary.
• No icons, no photographs of Valmont, Kessler, or anyone.

```html
<!DOCTYPE html>
<html lang="en">
<head>
<meta charset="utf-8">
<title>The Liminal Remainder — Journal Cover Wrap</title>
<link rel="stylesheet" href="https://fonts.googleapis.com/css2?family=Arimo:wght@400;700&display=swap">
<style>
  :root {
    --paper: #ffffff;
    --ink: #111111;
    --magenta: #b5104f;
    --violet: #4f3a84;
    --sky: #9fd6ef;
    --blue: #3d7fcf;
    --deep: #161616;
    --crimson: #a3173a;
  }
  * { margin: 0; padding: 0; box-sizing: border-box; }
  html, body { width: 1200px; height: 1000px; overflow: hidden; background: var(--paper); }
  .wrap {
    position: relative;
    width: 1200px;
    height: 1000px;
    background: var(--paper);
    font-family: "Arimo", Arial, sans-serif;
    color: var(--ink);
  }
  .artwork {
    position: absolute;
    top: 215px;
    height: 700px;
  }
  .artwork--back { left: 0; width: 580px; opacity: 0.55; }
  .artwork--front { left: 618px; width: 582px; }
  .artwork svg { width: 100%; height: 100%; display: block; }

  .spine {
    position: absolute;
    left: 588px;
    top: 235px;
    width: 22px;
    height: 570px;
  }
  .spine__text {
    position: absolute;
    left: 50%;
    top: 50%;
    transform: translate(-50%, -50%) rotate(-90deg);
    white-space: nowrap;
    font-size: 13.5px;
    letter-spacing: 0.1px;
  }
  .spine__name { font-weight: 700; }
  .spine__name .first { color: var(--magenta); }
  .spine__name .second { color: var(--violet); }

  .front {
    position: absolute;
    left: 622px;
    top: 96px;
    width: 560px;
  }
  .issue-line {
    font-size: 14px;
    font-weight: 700;
    margin-left: 0;
  }
  .title {
    margin-top: 18px;
    text-align: center;
    font-weight: 700;
    line-height: 0.95;
    letter-spacing: 1px;
    font-size: 50px;
    padding-left: 30px;
  }
  .title .first { display: block; color: var(--magenta); }
  .title .second { display: block; color: var(--violet); }
  .subtitle {
    text-align: center;
    font-size: 29px;
    line-height: 1.08;
    margin-top: 4px;
    padding-left: 30px;
    font-weight: 400;
  }
</style>
</head>
<body>
<div class="wrap">

  <div class="artwork artwork--back" role="img" aria-label="Abstract symmetrical ink-blot in sky blue, blue, magenta and black above a split crimson and black cerebral form, faded for the back cover">
    <svg viewBox="0 0 580 700" preserveAspectRatio="none">
      <defs>
        <radialGradient id="blot-back" cx="50%" cy="45%" r="55%">
          <stop offset="0" stop-color="#161616"/>
          <stop offset="0.35" stop-color="#3d7fcf"/>
          <stop offset="0.7" stop-color="#9fd6ef"/>
          <stop offset="1" stop-color="#ffffff" stop-opacity="0"/>
        </radialGradient>
        <linearGradient id="form-back" x1="0" x2="1">
          <stop offset="0.5" stop-color="#a3173a"/>
          <stop offset="0.5" stop-color="#161616"/>
        </linearGradient>
      </defs>
      <ellipse cx="290" cy="220" rx="300" ry="200" fill="url(#blot-back)"/>
      <ellipse cx="276" cy="510" rx="140" ry="180" fill="url(#form-back)"/>
    </svg>
  </div>

  <div class="spine">
    <p class="spine__text"><span class="spine__name"><span class="first">THE LIMINAL</span> <span class="second">REMAINDER</span></span>&nbsp; A Journal of Deconstruction and Psychoanalysis&nbsp; Vol.1 No.1 2014</p>
  </div>

  <div class="artwork artwork--front" role="img" aria-label="Abstract symmetrical ink-blot in sky blue, blue, magenta and black above a split crimson and black cerebral form">
    <svg viewBox="0 0 582 700" preserveAspectRatio="none">
      <defs>
        <radialGradient id="blot-front" cx="50%" cy="45%" r="55%">
          <stop offset="0" stop-color="#161616"/>
          <stop offset="0.35" stop-color="#3d7fcf"/>
          <stop offset="0.7" stop-color="#9fd6ef"/>
          <stop offset="1" stop-color="#ffffff" stop-opacity="0"/>
        </radialGradient>
        <linearGradient id="form-front" x1="0" x2="1">
          <stop offset="0.5" stop-color="#a3173a"/>
          <stop offset="0.5" stop-color="#161616"/>
        </linearGradient>
      </defs>
      <ellipse cx="290" cy="220" rx="300" ry="200" fill="url(#blot-front)"/>
      <ellipse cx="290" cy="510" rx="140" ry="180" fill="url(#form-front)"/>
    </svg>
  </div>

  <header class="front">
    <p class="issue-line">Volume 1 Issue 1 2014</p>
    <h1 class="title"><span class="first">THE LIMINAL</span><span class="second">REMAINDER</span></h1>
    <p class="subtitle">A Journal of Deconstruction<br>and Psychoanalysis</p>
  </header>

</div>
</body>
</html>
```